Veterinary hospital brochure design

we need brochure design for our veterinary hospital, something interesting, catchy and unique. Once we get going we need to add few unique services we offer and should be highlighted.Nice colors, and should be very professional looking. Brochure to be tri fold, nice colors highlight our services.
Like shades of blues or green.This is full service veterinary hospital. We do focus and specialize in Canine reproduction.

pet owners

Hospital

Serif
Script

• catchy words
• unique design
• have our unique services included
• good pictures and catchy words etc etc

```html
<!DOCTYPE html>
<html lang="en">
<head>
<meta charset="utf-8">
<title>Oak Hollow Hospital for Animals – Reproduction Services</title>
<link rel="stylesheet" href="https://fonts.googleapis.com/css2?family=Allura&family=Didact+Gothic&family=Lato:wght@400;700&display=swap">
<style>
  :root {
    --paper: #ffffff;
    --fold-grey: #d9d9db;
    --script-blue: #4b5bab;
    --text-dark: #3a3a3c;
    --rule-grey: #8d8d90;
    --tick-orange: #ef8a5a;
    --paw-blue: #8c91d2;
    --paw-yellow: #e3e57a;
  }
  * { box-sizing: border-box; margin: 0; padding: 0; }
  html, body { width: 1200px; height: 855px; overflow: hidden; background: var(--paper); }
  .brochure {
    position: relative; width: 1200px; height: 855px; overflow: hidden;
    background: var(--paper);
    font-family: "Didact Gothic", "Century Gothic", sans-serif;
  }
  .inner-page {
    position: absolute; left: 255px; top: 0; width: 550px; height: 855px;
    background: linear-gradient(90deg, #e6e6e8 0%, #f7f7f8 10%, #ffffff 28%, #ffffff 86%, #f0f0f1 96%, var(--fold-grey) 100%);
  }
  .fold-shadow {
    position: absolute; left: 805px; top: 0; width: 30px; height: 855px;
    background: linear-gradient(90deg, rgba(0,0,0,0.10), rgba(0,0,0,0));
  }

  /* Photo areas: soft, feathered tone fields */
  .photo { position: absolute; }
  .photo--yorkie {
    left: -20px; top: -30px; width: 270px; height: 320px;
    background:
      radial-gradient(ellipse 45% 40% at 45% 48%, rgba(196,150,96,0.95), rgba(196,150,96,0) 100%),
      radial-gradient(ellipse 55% 50% at 45% 45%, rgba(92,70,52,0.95) 40%, rgba(92,70,52,0) 100%);
  }
  .photo--basset {
    left: -30px; top: 170px; width: 280px; height: 340px;
    background:
      radial-gradient(ellipse 35% 30% at 55% 45%, rgba(232,214,196,0.9), rgba(232,214,196,0) 100%),
      radial-gradient(ellipse 55% 50% at 50% 50%, rgba(140,88,50,0.95) 45%, rgba(140,88,50,0) 100%);
  }
  .photo--retriever {
    left: -40px; top: 360px; width: 380px; height: 540px;
    background:
      radial-gradient(ellipse 40% 30% at 50% 55%, rgba(246,222,190,0.95), rgba(246,222,190,0) 100%),
      radial-gradient(ellipse 55% 55% at 45% 55%, rgba(212,164,104,0.97) 50%, rgba(212,164,104,0) 100%);
  }
  .photo--kitten {
    left: 1010px; top: 60px; width: 220px; height: 220px;
    background: radial-gradient(ellipse 50% 48% at 55% 50%, rgba(236,200,176,0.97) 45%, rgba(236,200,176,0) 100%);
  }
  .photo--ginger-cat {
    left: 960px; top: 240px; width: 270px; height: 370px;
    background:
      radial-gradient(ellipse 30% 25% at 55% 60%, rgba(245,220,190,0.9), rgba(245,220,190,0) 100%),
      radial-gradient(ellipse 52% 50% at 55% 50%, rgba(218,134,66,0.97) 50%, rgba(218,134,66,0) 100%);
  }
  .photo--grey-cat {
    left: 960px; top: 570px; width: 270px; height: 320px;
    background: radial-gradient(ellipse 52% 55% at 55% 55%, rgba(122,128,133,0.97) 50%, rgba(122,128,133,0) 100%);
  }

  .headline {
    position: absolute; left: 322px; top: 82px;
    font-family: "Allura", cursive; font-weight: 400; color: var(--script-blue);
    font-size: 78px; line-height: 0.72; white-space: nowrap;
    transform: rotate(-7deg); transform-origin: left top;
  }
  .headline span { display: block; }
  .headline .line-two { padding-left: 52px; }

  .services-rule {
    position: absolute; left: 404px; top: 237px; width: 2px; height: 398px; background: var(--rule-grey);
  }
  .services {
    position: absolute; left: 414px; top: 251px; list-style: none;
    font-size: 17.5px; color: var(--text-dark); letter-spacing: -0.3px;
  }
  .services li { display: flex; align-items: center; height: 31.7px; white-space: nowrap; }
  .services svg { width: 24px; height: 20px; margin-right: 12px; flex: none; }

  .hospital-name {
    position: absolute; left: 438px; top: 630px; display: flex; align-items: center; gap: 10px;
    font-family: "Lato", sans-serif; font-weight: 400; color: var(--text-dark);
  }
  .hospital-name .mark { width: 26px; height: 26px; border-radius: 50%; border: 2px solid var(--text-dark); }
  .hospital-name .words { font-size: 17px; line-height: 1.1; letter-spacing: 0.5px; }

  .vet {
    position: absolute; left: 456px; top: 727px; font-family: "Lato", sans-serif; color: #1f1f21;
  }
  .vet-name { font-size: 14px; font-weight: 700; }
  .vet-specialty { font-size: 12.5px; margin-top: 12px; }

  .paw { position: absolute; width: 80px; height: 76px; }
  .paw--blue { fill: var(--paw-blue); }
  .paw--yellow { fill: var(--paw-yellow); }
</style>
</head>
<body>
<main class="brochure">
  <div class="inner-page"></div>
  <div class="fold-shadow"></div>

  <div class="photo photo--basset" role="img" aria-label="Photo of a basset hound peeking in"></div>
  <div class="photo photo--yorkie" role="img" aria-label="Photo of a Yorkshire terrier with a red bow"></div>
  <div class="photo photo--retriever" role="img" aria-label="Photo of a smiling golden retriever"></div>
  <div class="photo photo--kitten" role="img" aria-label="Photo of a cream kitten meowing"></div>
  <div class="photo photo--ginger-cat" role="img" aria-label="Photo of a ginger Maine Coon cat"></div>
  <div class="photo photo--grey-cat" role="img" aria-label="Photo of a grey Scottish Fold cat"></div>

  <svg class="paw paw--blue" style="left:918px;top:78px" viewBox="0 0 80 76"><ellipse cx="40" cy="52" rx="20" ry="17"/><ellipse cx="15" cy="32" rx="8" ry="11"/><ellipse cx="30" cy="16" rx="8" ry="11"/><ellipse cx="50" cy="16" rx="8" ry="11"/><ellipse cx="65" cy="32" rx="8" ry="11"/></svg>
  <svg class="paw paw--blue" style="left:830px;top:140px" viewBox="0 0 80 76"><ellipse cx="40" cy="52" rx="20" ry="17"/><ellipse cx="15" cy="32" rx="8" ry="11"/><ellipse cx="30" cy="16" rx="8" ry="11"/><ellipse cx="50" cy="16" rx="8" ry="11"/><ellipse cx="65" cy="32" rx="8" ry="11"/></svg>
  <svg class="paw paw--blue" style="left:886px;top:252px" viewBox="0 0 80 76"><ellipse cx="40" cy="52" rx="20" ry="17"/><ellipse cx="15" cy="32" rx="8" ry="11"/><ellipse cx="30" cy="16" rx="8" ry="11"/><ellipse cx="50" cy="16" rx="8" ry="11"/><ellipse cx="65" cy="32" rx="8" ry="11"/></svg>
  <svg class="paw paw--yellow" style="left:832px;top:432px;width:104px;height:98px" viewBox="0 0 80 76"><ellipse cx="40" cy="52" rx="20" ry="17"/><ellipse cx="15" cy="32" rx="8" ry="11"/><ellipse cx="30" cy="16" rx="8" ry="11"/><ellipse cx="50" cy="16" rx="8" ry="11"/><ellipse cx="65" cy="32" rx="8" ry="11"/></svg>
  <svg class="paw paw--yellow" style="left:852px;top:610px;width:100px;height:94px" viewBox="0 0 80 76"><ellipse cx="40" cy="52" rx="20" ry="17"/><ellipse cx="15" cy="32" rx="8" ry="11"/><ellipse cx="30" cy="16" rx="8" ry="11"/><ellipse cx="50" cy="16" rx="8" ry="11"/><ellipse cx="65" cy="32" rx="8" ry="11"/></svg>

  <h1 class="headline"><span class="line-one">&amp; We love</span><span class="line-two">care for them!</span></h1>

  <div class="services-rule"></div>
  <ul class="services">
    <li><svg viewBox="0 0 24 20"><path d="M3 10 L9 16 L21 3" fill="none" stroke="var(--tick-orange)" stroke-width="2.6" stroke-linecap="round" stroke-linejoin="round"/></svg>Breeding Soundness Exams</li>
    <li><svg viewBox="0 0 24 20"><path d="M3 10 L9 16 L21 3" fill="none" stroke="var(--tick-orange)" stroke-width="2.6" stroke-linecap="round" stroke-linejoin="round"/></svg>Semen Collection</li>
    <li><svg viewBox="0 0 24 20"><path d="M3 10 L9 16 L21 3" fill="none" stroke="var(--tick-orange)" stroke-width="2.6" stroke-linecap="round" stroke-linejoin="round"/></svg>Computer Assisted Semen Analysis</li>
    <li><svg viewBox="0 0 24 20"><path d="M3 10 L9 16 L21 3" fill="none" stroke="var(--tick-orange)" stroke-width="2.6" stroke-linecap="round" stroke-linejoin="round"/></svg>Caesarian Sections</li>
    <li><svg viewBox="0 0 24 20"><path d="M3 10 L9 16 L21 3" fill="none" stroke="var(--tick-orange)" stroke-width="2.6" stroke-linecap="round" stroke-linejoin="round"/></svg>Ovulation Timing</li>
    <li><svg viewBox="0 0 24 20"><path d="M3 10 L9 16 L21 3" fill="none" stroke="var(--tick-orange)" stroke-width="2.6" stroke-linecap="round" stroke-linejoin="round"/></svg>Infertility Work-Ups</li>
    <li><svg viewBox="0 0 24 20"><path d="M3 10 L9 16 L21 3" fill="none" stroke="var(--tick-orange)" stroke-width="2.6" stroke-linecap="round" stroke-linejoin="round"/></svg>Transcervical Insemination</li>
    <li><svg viewBox="0 0 24 20"><path d="M3 10 L9 16 L21 3" fill="none" stroke="var(--tick-orange)" stroke-width="2.6" stroke-linecap="round" stroke-linejoin="round"/></svg>Surgical Insemination</li>
    <li><svg viewBox="0 0 24 20"><path d="M3 10 L9 16 L21 3" fill="none" stroke="var(--tick-orange)" stroke-width="2.6" stroke-linecap="round" stroke-linejoin="round"/></svg>Pregnancy Ultrasound</li>
    <li><svg viewBox="0 0 24 20"><path d="M3 10 L9 16 L21 3" fill="none" stroke="var(--tick-orange)" stroke-width="2.6" stroke-linecap="round" stroke-linejoin="round"/></svg>Semen Freezing</li>
  </ul>

  <div class="hospital-name">
    <span class="mark"></span>
    <span class="words">OAK HOLLOW<br>HOSPITAL FOR ANIMALS</span>
  </div>

  <div class="vet">
    <p class="vet-name">Dr. Marcus Ellery DVM</p>
    <p class="vet-specialty">Expertise in Canine Reproduction and Infertility</p>
  </div>
</main>
</body>
</html>
```